KVR Biz Cards

We are a property management company that manages luxury level residential estates. As such, we need a business card design that gives a high end feel. The idea at the moment is to list the services offered on the back of the card, and our company information on the front of the card.

Services for the back of the card are as follows:
Professional Property Management service, Home Hosting & Concierge Service, Holliday Home / Income Property Management

```html
<!DOCTYPE html>
<html lang="en">
<head>
<meta charset="utf-8">
<title>KVR Business Cards</title>
<link rel="stylesheet" href="https://fonts.googleapis.com/css2?family=Roboto:wght@400;500;700&display=swap">
<style>
  :root {
    --backdrop: #5e3d22;
    --bronze: #875a32;
    --bronze-deep: #7d5533;
    --paper: #f3f2f0;
    --ink: #0a0a0a;
    --white: #ffffff;
    --sand: #d9cbbb;
  }
  * { box-sizing: border-box; margin: 0; padding: 0; }
  html, body { width: 1200px; height: 800px; overflow: hidden; }
  body {
    background: var(--backdrop);
    font-family: "Roboto", Arial, sans-serif;
    position: relative;
  }
  .card {
    position: absolute;
    top: 120px;
    width: 320px;
    height: 560px;
    background: var(--paper);
    overflow: hidden;
  }
  .card--services { left: 250px; }
  .card--contact { left: 630px; }

  /* Services side */
  .brand-panel {
    position: absolute; left: 0; top: 0; width: 100%; height: 218px;
    background: linear-gradient(135deg, var(--bronze) 40%, var(--bronze-deep));
  }
  .brand {
    position: absolute; left: 0; width: 100%; text-align: center;
  }
  .brand__mark {
    display: inline-flex; align-items: center; gap: 8px;
    font-weight: 500; font-size: 30px; letter-spacing: 1px; line-height: 1;
  }
  .brand__square { width: 14px; height: 14px; }
  .brand__name {
    display: block; font-weight: 500; font-size: 12.5px; letter-spacing: 0.6px;
    margin-top: 10px;
  }
  .brand__tagline {
    display: block; font-size: 8.5px; letter-spacing: 0.5px; margin-top: 1px;
  }
  .card--services .brand { top: 86px; }
  .card--services .brand__mark { color: var(--white); }
  .card--services .brand__square { background: var(--white); }
  .card--services .brand__name { color: var(--ink); }
  .card--services .brand__tagline { color: var(--white); }

  .services-title {
    position: absolute; left: 0; top: 248px; width: 100%; text-align: center;
    font-weight: 700; font-size: 22px; color: var(--ink); letter-spacing: -0.2px;
  }
  .service {
    position: absolute; left: 0; width: 100%; height: 53px;
    background: linear-gradient(90deg, var(--bronze), var(--bronze-deep));
    color: var(--white); font-size: 15px; line-height: 18.5px;
    display: flex; align-items: center; justify-content: center; text-align: center;
  }
  .service--1 { top: 308px; }
  .service--2 { top: 386px; }
  .service--3 { top: 464px; }

  /* Contact side */
  .watermark {
    position: absolute; left: 0; top: 188px; width: 100%; text-align: center;
    font-weight: 700; font-size: 104px; letter-spacing: 8px; line-height: 1;
    color: var(--sand);
  }
  .card--contact .brand { top: 76px; }
  .card--contact .brand__mark { color: var(--bronze); }
  .card--contact .brand__square { background: var(--bronze); }
  .card--contact .brand__name { color: var(--ink); }
  .card--contact .brand__tagline { color: var(--bronze); }

  .person { position: absolute; left: 32px; top: 304px; }
  .person__name {
    font-weight: 700; font-size: 22px; color: var(--bronze); letter-spacing: -0.2px;
  }
  .person__title { font-size: 17px; color: var(--ink); margin-top: 2px; }

  .contact-panel {
    position: absolute; left: 0; top: 361px; width: 100%; height: 199px;
    background: var(--ink); color: var(--white);
  }
  .contact-list { list-style: none; position: absolute; left: 30px; top: 36px; }
  .contact-list li {
    display: flex; align-items: flex-start; gap: 14px;
    font-size: 15px; line-height: 18.5px; margin-bottom: 18px;
  }
  .contact-list svg { width: 13px; height: 13px; flex: none; margin-top: 1px; fill: var(--white); }
</style>
</head>
<body>
  <section class="card card--services">
    <div class="brand-panel"></div>
    <div class="brand">
      <span class="brand__mark"><span class="brand__square"></span>KVR</span>
      <span class="brand__name">KESTREL VALE MANAGEMENT</span>
      <span class="brand__tagline">Crafted Care for Every Fine Residence</span>
    </div>
    <h2 class="services-title">SERVICES</h2>
    <div class="service service--1">Professional Property<br>Management service</div>
    <div class="service service--2">Home Hosting &amp; Concierge<br>Service</div>
    <div class="service service--3">Holliday Home / Income<br>Property Management</div>
  </section>

  <section class="card card--contact">
    <div class="watermark" aria-hidden="true">KVR</div>
    <div class="brand">
      <span class="brand__mark"><span class="brand__square"></span>KVR</span>
      <span class="brand__name">KESTREL VALE MANAGEMENT</span>
      <span class="brand__tagline">Crafted Care for Every Fine Residence</span>
    </div>
    <div class="person">
      <div class="person__name">YOUR NAME</div>
      <div class="person__title">TITLE</div>
    </div>
    <div class="contact-panel">
      <ul class="contact-list">
        <li>
          <svg viewBox="0 0 24 24" aria-hidden="true"><path d="M6.6 10.8a15 15 0 0 0 6.6 6.6l2.2-2.2c.3-.3.7-.4 1-.2 1.1.4 2.3.6 3.6.6.6 0 1 .4 1 1V20c0 .6-.4 1-1 1A17 17 0 0 1 3 4c0-.6.4-1 1-1h3.5c.6 0 1 .4 1 1 0 1.3.2 2.5.6 3.6.1.3 0 .7-.2 1z"/></svg>
          <span>012-345-6789</span>
        </li>
        <li>
          <svg viewBox="0 0 24 24" aria-hidden="true"><path d="M2 4h20v16H2zm2 2v.5l8 5 8-5V6zm0 2.9V18h16V8.9l-8 5z"/></svg>
          <span>hello@kestrelvale.com</span>
        </li>
        <li>
          <svg viewBox="0 0 24 24" aria-hidden="true"><path d="M12 2a7 7 0 0 0-7 7c0 5.2 7 13 7 13s7-7.8 7-13a7 7 0 0 0-7-7zm0 9.5A2.5 2.5 0 1 1 12 6.5a2.5 2.5 0 0 1 0 5z"/></svg>
          <span>107&nbsp; xyz Street,<br>ABC 35816</span>
        </li>
      </ul>
    </div>
  </section>
</body>
</html>
```